Business card design for global fintech startup

Veltrix is a modern payments platform for the global insurance industry, serving international health, life, and travel insurers, MGAs, brokers, and partners.

We need a professional, premium business card for use at insurance conferences and executive meetings. The goal is to create a card that feels trustworthy, modern, and high-quality, while still being distinctive and memorable in a stack of business cards.

Target audience:
Senior insurance executives (VP, C-suite).

Design goals:
Clear, professional, and credible
Modern but not trendy
Premium and well-structured
Easy to read and practical for networking

Brand direction:
Brand-first (company over individual)
Follow existing brand guidelines where possible
Clean layout, strong hierarchy, excellent readability

Must include:
Name
Title
Company name (Veltrix)
Logo
Email
Phone/Whatsapp
Website (www.withveltrix.example)
Tagline - Payments Built On Trust

Materials & finish:
Open to designer recommendations for premium look and feel.

Please avoid:
Flashy or trendy startup styles
Generic insurance icons or clichés
Cluttered layouts or hard-to-read text

Deliverables:
Front and back business card, print-ready files.

Target Market(s)

Global Insurance executives

Industry/Entity Type

Fintech, Insurtech, Insurance, Financial Services

Contact Information for Business Card

Name Title Company name (Veltrix) Logo Email Phone/Whatsapp Website (www.withveltrix.example) Tagline - Payments Built On Trust

Font styles to use
Other font styles liked:
• See brand guidelines

Requirements
Nice to have
• something that stands out/makes us more memorable while still remaining professional
Should not have
• Please avoid: Flashy or trendy startup styles Generic insurance icons or clichés Cluttered layouts or hard-to-read text

```html
<!DOCTYPE html>
<html lang="en">
<head>
<meta charset="utf-8">
<title>Veltrix Business Card — Front and Back</title>
<link href="https://fonts.googleapis.com/css2?family=Open+Sans:ital,wght@0,400;0,600;0,700;1,400&display=swap" rel="stylesheet">
<style>
  :root {
    --stage: #1b1b1d;
    --card-dark: #231f20;
    --card-light: #d8d8d8;
    --ink: #1a1a1a;
    --ink-soft: #2e2e2e;
    --map-tone: #3d3a3b;
    --band-purple: #5b4496;
    --band-blue: #3a63a8;
    --band-teal: #2b9bc6;
    --accent-orange: #e39a2d;
    --brand-light: #e6e6e6;
  }
  * { box-sizing: border-box; margin: 0; padding: 0; }
  html, body {
    width: 1200px; height: 800px; overflow: hidden;
    background: var(--stage);
    font-family: "Open Sans", Arial, sans-serif;
  }
  .stage {
    width: 1200px; height: 800px;
    display: flex; align-items: center; justify-content: center; gap: 40px;
  }
  .card {
    position: relative;
    width: 520px; height: 297px;
    border-radius: 22px;
    overflow: hidden;
  }

  /* Back */
  .card--back { background: var(--card-dark); }
  .card-back__map {
    position: absolute; left: 90px; top: 30px; width: 340px; height: 237px;
    background: radial-gradient(ellipse at 50% 50%, var(--map-tone) 0%, rgba(61,58,59,0.6) 50%, rgba(35,31,32,0) 72%);
  }
  .card-back__brand {
    position: absolute; inset: 0;
    display: flex; align-items: center; justify-content: center; gap: 12px;
  }
  .brand-dot {
    width: 18px; height: 18px; border-radius: 50%;
    background: var(--accent-orange);
  }
  .card-back__name {
    font-weight: 600; font-size: 44px; letter-spacing: 3px;
    color: var(--brand-light);
  }

  /* Front */
  .card--front { background: var(--card-light); }
  .card-front__brand {
    position: absolute; left: 40px; top: 26px;
    display: flex; align-items: center; gap: 12px;
  }
  .card-front__name {
    font-weight: 600; font-size: 42px; letter-spacing: 3px; color: var(--ink);
  }
  .person { position: absolute; left: 40px; top: 98px; }
  .person__name { font-weight: 700; font-size: 20px; color: var(--ink); line-height: 1.2; }
  .person__title { font-size: 12.5px; color: var(--ink-soft); line-height: 1.4; }
  .person__rule {
    position: absolute; left: 200px; top: 137px; width: 290px; height: 1px;
    background: var(--ink);
  }
  .contacts { position: absolute; left: 40px; top: 152px; list-style: none; }
  .contacts li {
    display: flex; align-items: center; gap: 8px;
    font-size: 11.5px; color: var(--ink); line-height: 18px;
  }
  .contacts svg { width: 11px; height: 11px; flex: none; }
  .band { position: absolute; left: 0; bottom: 0; width: 520px; height: 297px; }
  .tagline {
    position: absolute; right: 30px; bottom: 20px;
    font-size: 13px; font-weight: 600; color: #ffffff; letter-spacing: 0.3px;
  }
</style>
</head>
<body>
<main class="stage">

  <section class="card card--back" aria-label="Business card back">
    <div class="card-back__map" role="img" aria-label="Dotted world map in dark grey behind the company name"></div>
    <div class="card-back__brand">
      <span class="brand-dot"></span>
      <span class="card-back__name">VELTRIX</span>
    </div>
  </section>

  <section class="card card--front" aria-label="Business card front">
    <svg class="band" viewBox="0 0 520 297" aria-hidden="true">
      <defs>
        <linearGradient id="bandGradient" x1="0" y1="0" x2="1" y2="0">
          <stop offset="0" stop-color="var(--band-purple)"/>
          <stop offset="0.5" stop-color="var(--band-blue)"/>
          <stop offset="1" stop-color="var(--band-teal)"/>
        </linearGradient>
      </defs>
      <path d="M0 262 C120 262 170 286 270 262 C360 240 420 212 520 214 L520 297 L0 297 Z" fill="url(#bandGradient)"/>
      <path d="M0 256 C120 256 170 280 270 256 C360 234 420 206 520 208" fill="none" stroke="var(--accent-orange)" stroke-width="2"/>
    </svg>

    <div class="card-front__brand">
      <span class="brand-dot"></span>
      <span class="card-front__name">VELTRIX</span>
    </div>

    <div class="person">
      <p class="person__name">Daniel Reyes</p>
      <p class="person__title">Chief Executive Officer</p>
    </div>
    <span class="person__rule"></span>

    <ul class="contacts">
      <li>
        <svg viewBox="0 0 12 12"><circle cx="6" cy="6" r="6" fill="var(--ink)"/><path d="M4 3.2 L5 3 L5.6 4.6 L5 5.2 C5.4 6 6 6.6 6.8 7 L7.4 6.4 L9 7 L8.8 8 C8 8.8 6 8.4 4.6 7 C3.4 5.8 3.2 4 4 3.2 Z" fill="var(--card-light)"/></svg>
        +10 20 3040 5060
      </li>
      <li>
        <svg viewBox="0 0 12 12"><rect x="0.5" y="2" width="11" height="8" fill="var(--ink)"/><path d="M1 2.5 L6 6.5 L11 2.5" fill="none" stroke="var(--card-light)" stroke-width="1"/></svg>
        dreyes@veltrix.example
      </li>
      <li>
        <svg viewBox="0 0 12 12"><circle cx="6" cy="6" r="5.5" fill="var(--ink)"/><path d="M0.5 6 H11.5 M6 0.5 C3 3 3 9 6 11.5 M6 0.5 C9 3 9 9 6 11.5" fill="none" stroke="var(--card-light)" stroke-width="0.8"/></svg>
        www.withveltrix.example
      </li>
    </ul>

    <p class="tagline">Payments Built On Trust</p>
  </section>

</main>
</body>
</html>
```